Flyer-Design für renomiertes Kosmetikstudio
Zielgruppe
Renomiertes Kosmetikstudio sucht hochwertiges Design für neue Flyer.
Zielgruppe Männer + Frauen die auf ihr Äußeres viel Wert legen.
Aufgabenstellung
Geradliniges Desgin unter Berücksichtigung von ganzheitlichen Farben (chakren). Edel.
Wir hätten gerne ein Angebot für Männer als auch für Frauen. Evtl. Aufteilung in 2 getrennte Flyer oder Flyer auf einer Seite Männer und umgedreht auf der anderen Seite für Frauen.?
Behandlungsbereiche die aufgenommen werden müssten:
Frauen
- Wimpernverlängerung
- Wimpernlifting
- Kosmetikbehandlung (Fresh Start - Encore Konzept) ausführlicher text dazu
zzgl. möglichen Bausteinen
- Fußpflege
- Nageldesign
- Enthaarung mit Zuckerpaste
- Massagen
Männer:
- Kosmetikbehandlung
- Maniküre
-- Massage
- Enthaarung
Für die Kosmetik hätte ich gerne jeweils 1 Seite komplett um hier mehr Infos rein zu packen zur FRESH START Behandlung.
Platz für Preise der Behandlungen und bausteine.
Gewünscht Din Lang Format, gerne aber auch offen für neue Ideen.

```html
<!DOCTYPE html>
<html lang="de">
<head>
<meta charset="utf-8">
<title>Lumara – Preisliste</title>
<link href="https://fonts.googleapis.com/css2?family=Montserrat:wght@400;500;600;700&family=Great+Vibes&display=swap" rel="stylesheet">
<style>
  :root{
    --pink:#e6177e;
    --pink-soft:#f08cb8;
    --indigo:#4f50a3;
    --violet:#8d2f8f;
    --orange:#e8792a;
    --green:#3cb44a;
    --yellow:#f1c232;
    --red:#e3232d;
    --text:#444;
    --ink:#3a3a3a;
    --muted:#777;
    --rule:#e2e2e2;
    --page:#ffffff;
    --canvas:#eeeeee;
  }
  *{box-sizing:border-box;margin:0;padding:0}
  html,body{width:1200px;height:3746px;overflow:hidden}
  body{background:var(--canvas);font-family:"Montserrat",sans-serif;color:var(--text);
    display:flex;flex-direction:column;justify-content:space-evenly;align-items:center}
  .spread{position:relative;width:1160px;background:var(--page);border:1px solid #ddd;overflow:hidden}
  .spread--outside{height:624px}
  .spread--inside{height:628px}
  .art{position:absolute;left:0;top:0}
  .section{position:absolute;width:250px;padding-left:12px}
  .section::before{content:"";position:absolute;left:0;top:0;width:6px;height:36px;background:var(--accent)}
  .section h2{font-weight:500;font-size:15px;line-height:20px;margin-bottom:4px;color:var(--text)}
  .price-table{width:238px;font-size:8px}
  .price-table .head{background:var(--head,var(--indigo));color:#fff;font-weight:700;font-size:8px;
    line-height:12px;padding-left:4px;margin-bottom:2px}
  .row{display:flex;align-items:center;line-height:13px;border-bottom:1px solid var(--rule)}
  .row .svc{flex:1;padding-left:4px}
  .row .svc.two{line-height:10px;padding:1px 0 1px 4px}
  .row .dur{width:52px;display:flex;align-items:center;gap:4px;color:var(--muted);border-left:1px solid var(--rule);padding-left:4px}
  .row .dur::before{content:"";width:7px;height:7px;border:1px solid var(--muted);border-radius:50%}
  .row .price{width:42px;text-align:right;padding-right:4px;border-left:1px solid var(--rule)}
  .gap{height:8px;border-bottom:1px solid var(--rule)}
  .price-table--pink{--head:var(--pink)}
  .price-table--pink .price{color:var(--pink-soft)}
  .brand{position:absolute;text-align:center;color:var(--ink)}
  .brand .name{font-weight:500;font-size:34px;line-height:40px;letter-spacing:1px}
  .brand .tag{font-weight:500;font-size:12px;letter-spacing:1px}
  .brand--small .name{font-size:17px;line-height:20px}
  .brand--small .tag{font-size:6px}
  .cover-title{position:absolute;left:900px;top:222px;font-size:19px;letter-spacing:.5px;padding-left:16px}
  .cover-title::before{content:"";position:absolute;left:0;top:-4px;width:6px;height:32px;background:var(--pink)}
  .contact{position:absolute;left:640px;top:405px;width:200px;padding-left:16px;font-size:7.5px;line-height:11px;color:var(--muted)}
  .contact::before{content:"";position:absolute;left:0;top:0;width:6px;height:34px;background:var(--red)}
  .contact h3{font-weight:500;font-size:15px;line-height:20px;color:var(--text);margin-bottom:8px}
  .contact p{margin-bottom:10px}
  .intro{position:absolute;left:780px;top:368px;width:370px;font-size:8px;line-height:12px;color:var(--muted)}
  .signature{position:absolute;left:780px;top:452px;font-family:"Great Vibes",cursive;font-size:58px;color:#222;line-height:64px}
  .subtitle{position:absolute;left:752px;top:540px;font-size:20px;color:var(--text)}
</style>
</head>
<body>

<section class="spread spread--outside">
  <svg class="art" width="1160" height="624" viewBox="0 0 1160 624">
    <defs>
      <linearGradient id="skinA" x1="0" y1="0" x2="1" y2="1"><stop offset="0" stop-color="#f3ede8"/><stop offset=".6" stop-color="#d9b9a6"/><stop offset="1" stop-color="#f1f1f1"/></linearGradient>
      <linearGradient id="skinB" x1="0" y1="0" x2="1" y2="1"><stop offset="0" stop-color="#f4f2f1"/><stop offset=".55" stop-color="#e2c2ad"/><stop offset="1" stop-color="#c99c84"/></linearGradient>
    </defs>
    <path d="M0 0H296V300C220 278 120 330 0 312Z" fill="url(#skinA)" role="img" aria-label="Foto: Mann mit Gesichtsmaske bei der Kosmetikbehandlung"/>
    <path d="M0 312C120 330 220 278 296 300" stroke="var(--indigo)" stroke-width="9" fill="none"/>
    <path d="M700 0C800 12 900 46 1000 42C1080 38 1130 22 1160 14V0Z" fill="var(--pink)"/>
    <path d="M857 330C960 300 1060 350 1160 318V624H857Z" fill="url(#skinB)" role="img" aria-label="Foto: Frau mit Creme an der Wange"/>
    <path d="M580 324C680 340 760 300 860 300C960 300 1060 290 1160 292" stroke="var(--indigo)" stroke-width="9" fill="none"/>
    <path d="M857 330C960 300 1060 350 1160 318" stroke="var(--pink)" stroke-width="10" fill="none"/>
  </svg>

  <div class="section" style="left:30px;top:360px;--accent:var(--indigo)">
    <h2>Kosmetikbehandlung</h2>
    <div class="price-table"><div class="head">Kosmetik</div>
      <div class="row"><span class="svc">Lorem ipsum</span><span class="dur">20 min</span><span class="price">€ 17,00</span></div>
      <div class="row"><span class="svc">Dolor sit amet</span><span class="dur">45 min</span><span class="price">€ 29,00</span></div>
      <div class="row"><span class="svc two">Consectetur adipiscingt<br>Duis ultricies</span><span class="dur">90 min</span><span class="price">€ 64,50</span></div>
      <div class="gap"></div>
      <div class="row"><span class="svc">Nibh cursus</span><span class="dur">75 min</span><span class="price">€ 46,50</span></div>
      <div class="row"><span class="svc">Bibendum turpis</span><span class="dur">60 min</span><span class="price">€ 39,50</span></div>
      <div class="row"><span class="svc">sollicitudin</span><span class="dur">45 min</span><span class="price">€ 20,00</span></div>
      <div class="row"><span class="svc">Curabitur orci ipsum</span><span class="dur">35 min</span><span class="price">€ 35,00</span></div>
      <div class="row"><span class="svc">Nibh cursus</span><span class="dur">75 min</span><span class="price">€ 46,50</span></div>
      <div class="row"><span class="svc">Bibendum turpis</span><span class="dur">60 min</span><span class="price">€ 39,50</span></div>
      <div class="row"><span class="svc">sollicitudin</span><span class="dur">45 min</span><span class="price">€ 20,00</span></div>
      <div class="row"><span class="svc">Curabitur orci ipsum</span><span class="dur">35 min</span><span class="price">€ 35,00</span></div>
    </div>
  </div>

  <div class="section" style="left:312px;top:40px;--accent:var(--violet)">
    <h2>Maniküre</h2>
    <div class="price-table"><div class="head">Maniküre</div>
      <div class="row"><span class="svc">Lorem ipsum</span><span class="dur">20 min</span><span class="price">€ 17,00</span></div>
      <div class="row"><span class="svc">Dolor sit amet</span><span class="dur">45 min</span><span class="price">€ 29,00</span></div>
      <div class="row"><span class="svc two">Consectetur adipiscingt<br>Duis ultricies</span><span class="dur">90 min</span><span class="price">€ 64,50</span></div>
      <div class="gap"></div>
      <div class="row"><span class="svc">Nibh cursus</span><span class="dur">75 min</span><span class="price">€ 46,50</span></div>
      <div class="row"><span class="svc">Bibendum turpis</span><span class="dur">60 min</span><span class="price">€ 39,50</span></div>
      <div class="row"><span class="svc">sollicitudin</span><span class="dur">45 min</span><span class="price">€ 20,00</span></div>
    </div>
  </div>

  <div class="section" style="left:312px;top:202px;--accent:var(--green)">
    <h2>Fußpflege</h2>
    <div class="price-table"><div class="head">Fußpflege</div>
      <div class="row"><span class="svc">Lorem ipsum</span><span class="dur">20 min</span><span class="price">€ 17,00</span></div>
      <div class="row"><span class="svc">Dolor sit amet</span><span class="dur">45 min</span><span class="price">€ 29,00</span></div>
      <div class="row"><span class="svc two">Consectetur adipiscingt<br>Duis ultricies</span><span class="dur">90 min</span><span class="price">€ 64,50</span></div>
      <div class="gap"></div>
      <div class="row"><span class="svc">Nibh cursus</span><span class="dur">75 min</span><span class="price">€ 46,50</span></div>
      <div class="row"><span class="svc">Bibendum turpis</span><span class="dur">60 min</span><span class="price">€ 39,50</span></div>
      <div class="row"><span class="svc">sollicitudin</span><span class="dur">45 min</span><span class="price">€ 20,00</span></div>
    </div>
  </div>

  <div class="section" style="left:312px;top:360px;--accent:var(--yellow)">
    <h2>Massage</h2>
    <div class="price-table"><div class="head">Massage</div>
      <div class="row"><span class="svc">Lorem ipsum</span><span class="dur">20 min</span><span class="price">€ 17,00</span></div>
      <div class="row"><span class="svc">Dolor sit amet</span><span class="dur">45 min</span><span class="price">€ 29,00</span></div>
      <div class="row"><span class="svc two">Consectetur adipiscingt<br>Duis ultricies</span><span class="dur">90 min</span><span class="price">€ 64,50</span></div>
      <div class="gap"></div>
      <div class="row"><span class="svc">Nibh cursus</span><span class="dur">75 min</span><span class="price">€ 46,50</span></div>
      <div class="row"><span class="svc">Bibendum turpis</span><span class="dur">60 min</span><span class="price">€ 39,50</span></div>
      <div class="row"><span class="svc">sollicitudin</span><span class="dur">45 min</span><span class="price">€ 20,00</span></div>
      <div class="row"><span class="svc">Curabitur orci ipsum</span><span class="dur">35 min</span><span class="price">€ 35,00</span></div>
      <div class="row"><span class="svc">Nibh cursus</span><span class="dur">75 min</span><span class="price">€ 46,50</span></div>
      <div class="row"><span class="svc">Bibendum turpis</span><span class="dur">60 min</span><span class="price">€ 39,50</span></div>
      <div class="row"><span class="svc">sollicitudin</span><span class="dur">45 min</span><span class="price">€ 20,00</span></div>
      <div class="row"><span class="svc">Curabitur orci ipsum</span><span class="dur">35 min</span><span class="price">€ 35,00</span></div>
    </div>
  </div>

  <div class="section" style="left:596px;top:40px;--accent:var(--orange)">
    <h2>Enthaarung</h2>
    <div class="price-table"><div class="head">Enthaarung</div>
      <div class="row"><span class="svc">Lorem ipsum</span><span class="dur">20 min</span><span class="price">€ 17,00</span></div>
      <div class="row"><span class="svc">Dolor sit amet</span><span class="dur">45 min</span><span class="price">€ 29,00</span></div>
      <div class="row"><span class="svc two">Consectetur adipiscingt<br>Duis ultricies</span><span class="dur">90 min</span><span class="price">€ 64,50</span></div>
      <div class="gap"></div>
      <div class="row"><span class="svc">Nibh cursus</span><span class="dur">75 min</span><span class="price">€ 46,50</span></div>
      <div class="row"><span class="svc">Bibendum turpis</span><span class="dur">60 min</span><span class="price">€ 39,50</span></div>
      <div class="row"><span class="svc">sollicitudin</span><span class="dur">45 min</span><span class="price">€ 20,00</span></div>
      <div class="row"><span class="svc">Curabitur orci ipsum</span><span class="dur">35 min</span><span class="price">€ 35,00</span></div>
      <div class="row"><span class="svc">Nibh cursus</span><span class="dur">75 min</span><span class="price">€ 46,50</span></div>
      <div class="row"><span class="svc">Bibendum turpis</span><span class="dur">60 min</span><span class="price">€ 39,50</span></div>
      <div class="row"><span class="svc">sollicitudin</span><span class="dur">45 min</span><span class="price">€ 20,00</span></div>
      <div class="row"><span class="svc">Curabitur orci ipsum</span><span class="dur">35 min</span><span class="price">€ 35,00</span></div>
      <div class="row"><span class="svc">sollicitudin</span><span class="dur">45 min</span><span class="price">€ 20,00</span></div>
      <div class="row"><span class="svc">Curabitur orci ipsum</span><span class="dur">35 min</span><span class="price">€ 35,00</span></div>
    </div>
  </div>

  <div class="contact">
    <h3>KONTAKT</h3>
    <p>Lindenweg 14, 80000 Musterstadt<br>0123 45 67 890 | info@lumara-studio.de</p>
    <p>ÖFFNUNGSZEITEN<br>MO – DO 9:00 - 18:00 Uhr,<br>FR 9:00 - 16:00 Uhr<br>Weitere Termine gerne<br>nach Absprache.</p>
  </div>

  <div class="brand" style="left:880px;top:100px;width:260px">
    <div class="name">Lumara</div>
    <div class="tag">PFLEGE UND GELASSENHEIT</div>
  </div>
  <div class="cover-title">PREISLISTE</div>
</section>

<section class="spread spread--inside">
  <svg class="art" width="1160" height="628" viewBox="0 0 1160 628">
    <defs>
      <linearGradient id="studio" x1="0" y1="0" x2="1" y2="1"><stop offset="0" stop-color="#efe6df"/><stop offset=".5" stop-color="#d8bfb0"/><stop offset="1" stop-color="#f5f1ee"/></linearGradient>
      <linearGradient id="skinC" x1="0" y1="0" x2="1" y2="1"><stop offset="0" stop-color="#f2ece8"/><stop offset=".6" stop-color="#dfbea9"/><stop offset="1" stop-color="#f6f3f1"/></linearGradient>
    </defs>
    <path d="M0 0H296V150C210 130 110 180 0 162Z" fill="url(#studio)" role="img" aria-label="Foto: Kosmetikerin behandelt eine Kundin im Studio"/>
    <path d="M0 162C110 180 210 130 296 150" stroke="var(--pink)" stroke-width="9" fill="none"/>
    <path d="M700 0C800 12 900 40 1000 36C1080 32 1130 18 1160 12V0Z" fill="var(--pink)"/>
    <path d="M577 330C640 312 700 318 760 330V628H577Z" fill="url(#skinC)" role="img" aria-label="Foto: Frauengesicht mit Pfeilen zur Liftingwirkung"/>
    <path d="M577 318C700 300 800 336 900 330C1000 324 1100 310 1160 318" stroke="var(--pink)" stroke-width="11" fill="none"/>
    <path d="M310 628C400 600 500 594 577 610V628Z" fill="var(--pink)"/>
  </svg>

  <div class="section" style="left:30px;top:192px;--accent:var(--red)">
    <h2>Wimpernverlängerung</h2>
    <div class="price-table price-table--pink"><div class="head">Wimpernverlängerung</div>
      <div class="row"><span class="svc">Lorem ipsum</span><span class="dur">20 min</span><span class="price">€ 17,00</span></div>
      <div class="row"><span class="svc">Dolor sit amet</span><span class="dur">45 min</span><span class="price">€ 29,00</span></div>
      <div class="row"><span class="svc two">Consectetur adipiscingt<br>Duis ultricies</span><span class="dur">90 min</span><span class="price">€ 64,50</span></div>
      <div class="gap"></div>
      <div class="row"><span class="svc">Nibh cursus</span><span class="dur">75 min</span><span class="price">€ 46,50</span></div>
      <div class="row"><span class="svc">Bibendum turpis</span><span class="dur">60 min</span><span class="price">€ 39,50</span></div>
      <div class="row"><span class="svc">sollicitudin</span><span class="dur">45 min</span><span class="price">€ 20,00</span></div>
      <div class="row"><span class="svc">Curabitur orci ipsum</span><span class="dur">35 min</span><span class="price">€ 35,00</span></div>
    </div>
  </div>

  <div class="section" style="left:30px;top:370px;--accent:var(--indigo)">
    <h2>Wimpernlifting</h2>
    <div class="price-table price-table--pink"><div class="head">Wimpernlifting</div>
      <div class="row"><span class="svc">Lorem ipsum</span><span class="dur">20 min</span><span class="price">€ 17,00</span></div>
      <div class="row"><span class="svc">Dolor sit amet</span><span class="dur">45 min</span><span class="price">€ 29,00</span></div>
      <div class="row"><span class="svc two">Consectetur adipiscingt<br>Duis ultricies</span><span class="dur">90 min</span><span class="price">€ 64,50</span></div>
      <div class="gap"></div>
      <div class="row"><span class="svc">Nibh cursus</span><span class="dur">75 min</span><span class="price">€ 46,50</span></div>
      <div class="row"><span class="svc">Bibendum turpis</span><span class="dur">60 min</span><span class="price">€ 39,50</span></div>
      <div class="row"><span class="svc">sollicitudin</span><span class="dur">45 min</span><span class="price">€ 20,00</span></div>
      <div class="row"><span class="svc">Curabitur orci ipsum</span><span class="dur">35 min</span><span class="price">€ 35,00</span></div>
      <div class="row"><span class="svc">Nibh cursus</span><span class="dur">75 min</span><span class="price">€ 46,50</span></div>
      <div class="row"><span class="svc">Bibendum turpis</span><span class="dur">60 min</span><span class="price">€ 39,50</span></div>
      <div class="row"><span class="svc">sollicitudin</span><span class="dur">45 min</span><span class="price">€ 20,00</span></div>
      <div class="row"><span class="svc">Curabitur orci ipsum</span><span class="dur">35 min</span><span class="price">€ 35,00</span></div>
    </div>
  </div>

  <div class="section" style="left:312px;top:52px;--accent:var(--green)">
    <h2>Fußpflege</h2>
    <div class="price-table price-table--pink"><div class="head">Fußpflege</div>
      <div class="row"><span class="svc">Lorem ipsum</span><span class="dur">20 min</span><span class="price">€ 17,00</span></div>
      <div class="row"><span class="svc">Dolor sit amet</span><span class="dur">45 min</span><span class="price">€ 29,00</span></div>
      <div class="row"><span class="svc two">Consectetur adipiscingt<br>Duis ultricies</span><span class="dur">90 min</span><span class="price">€ 64,50</span></div>
      <div class="gap"></div>
      <div class="row"><span class="svc">Nibh cursus</span><span class="dur">75 min</span><span class="price">€ 46,50</span></div>
      <div class="row"><span class="svc">Bibendum turpis</span><span class="dur">60 min</span><span class="price">€ 39,50</span></div>
      <div class="row"><span class="svc">sollicitudin</span><span class="dur">45 min</span><span class="price">€ 20,00</span></div>
      <div class="row"><span class="svc">Curabitur orci ipsum</span><span class="dur">35 min</span><span class="price">€ 35,00</span></div>
      <div class="row"><span class="svc">Nibh cursus</span><span class="dur">75 min</span><span class="price">€ 46,50</span></div>
      <div class="row"><span class="svc">Bibendum turpis</span><span class="dur">60 min</span><span class="price">€ 39,50</span></div>
      <div class="row"><span class="svc">sollicitudin</span><span class="dur">45 min</span><span class="price">€ 20,00</span></div>
      <div class="row"><span class="svc">Curabitur orci ipsum</span><span class="dur">35 min</span><span class="price">€ 35,00</span></div>
      <div class="row"><span class="svc">Nibh cursus</span><span class="dur">75 min</span><span class="price">€ 46,50</span></div>
      <div class="row"><span class="svc">Bibendum turpis</span><span class="dur">60 min</span><span class="price">€ 39,50</span></div>
      <div class="row"><span class="svc">sollicitudin</span><span class="dur">45 min</span><span class="price">€ 20,00</span></div>
    </div>
  </div>

  <div class="section" style="left:312px;top:366px;--accent:var(--yellow)">
    <h2>Nageldesign</h2>
    <div class="price-table price-table--pink"><div class="head">Nageldesign</div>
      <div class="row"><span class="svc">Lorem ipsum</span><span class="dur">20 min</span><span class="price">€ 17,00</span></div>
      <div class="row"><span class="svc">Dolor sit amet</span><span class="dur">45 min</span><span class="price">€ 29,00</span></div>
      <div class="row"><span class="svc two">Consectetur adipiscingt<br>Duis ultricies</span><span class="dur">90 min</span><span class="price">€ 64,50</span></div>
      <div class="gap"></div>
      <div class="row"><span class="svc">Nibh cursus</span><span class="dur">75 min</span><span class="price">€ 46,50</span></div>
      <div class="row"><span class="svc">Bibendum turpis</span><span class="dur">60 min</span><span class="price">€ 39,50</span></div>
      <div class="row"><span class="svc">sollicitudin</span><span class="dur">45 min</span><span class="price">€ 20,00</span></div>
      <div class="row"><span class="svc">Curabitur orci ipsum</span><span class="dur">35 min</span><span class="price">€ 35,00</span></div>
      <div class="row"><span class="svc">Nibh cursus</span><span class="dur">75 min</span><span class="price">€ 46,50</span></div>
      <div class="row"><span class="svc">Bibendum turpis</span><span class="dur">60 min</span><span class="price">€ 39,50</span></div>
      <div class="row"><span class="svc">Curabitur orci ipsum</span><span class="dur">35 min</span><span class="price">€ 35,00</span></div>
    </div>
  </div>

  <div class="section" style="left:596px;top:56px;--accent:var(--orange)">
    <h2>Enthaarung mit Zuckerpaste</h2>
    <div class="price-table price-table--pink"><div class="head">Enthaarung mit Zuckerpaste</div>
      <div class="row"><span class="svc">Lorem ipsum</span><span class="dur">20 min</span><span class="price">€ 17,00</span></div>
      <div class="row"><span class="svc">Dolor sit amet</span><span class="dur">45 min</span><span class="price">€ 29,00</span></div>
      <div class="row"><span class="svc two">Consectetur adipiscingt<br>Duis ultricies</span><span class="dur">90 min</span><span class="price">€ 64,50</span></div>
      <div class="gap"></div>
      <div class="row"><span class="svc">Nibh cursus</span><span class="dur">75 min</span><span class="price">€ 46,50</span></div>
      <div class="row"><span class="svc">Bibendum turpis</span><span class="dur">60 min</span><span class="price">€ 39,50</span></div>
      <div class="row"><span class="svc">sollicitudin</span><span class="dur">45 min</span><span class="price">€ 20,00</span></div>
      <div class="row"><span class="svc">Curabitur orci ipsum</span><span class="dur">35 min</span><span class="price">€ 35,00</span></div>
      <div class="row"><span class="svc">Nibh cursus</span><span class="dur">75 min</span><span class="price">€ 46,50</span></div>
      <div class="row"><span class="svc">Bibendum turpis</span><span class="dur">60 min</span><span class="price">€ 39,50</span></div>
      <div class="row"><span class="svc">sollicitudin</span><span class="dur">45 min</span><span class="price">€ 20,00</span></div>
      <div class="row"><span class="svc">Curabitur orci ipsum</span><span class="dur">35 min</span><span class="price">€ 35,00</span></div>
    </div>
  </div>

  <div class="section" style="left:876px;top:56px;--accent:var(--violet)">
    <h2>Massagen</h2>
    <div class="price-table price-table--pink"><div class="head">Enthaarung mit Zuckerpaste</div>
      <div class="row"><span class="svc">Lorem ipsum</span><span class="dur">20 min</span><span class="price">€ 17,00</span></div>
      <div class="row"><span class="svc">Dolor sit amet</span><span class="dur">45 min</span><span class="price">€ 29,00</span></div>
      <div class="row"><span class="svc two">Consectetur adipiscingt<br>Duis ultricies</span><span class="dur">90 min</span><span class="price">€ 64,50</span></div>
      <div class="gap"></div>
      <div class="row"><span class="svc">Nibh cursus</span><span class="dur">75 min</span><span class="price">€ 46,50</span></div>
      <div class="row"><span class="svc">Bibendum turpis</span><span class="dur">60 min</span><span class="price">€ 39,50</span></div>
      <div class="row"><span class="svc">sollicitudin</span><span class="dur">45 min</span><span class="price">€ 20,00</span></div>
      <div class="row"><span class="svc">Curabitur orci ipsum</span><span class="dur">35 min</span><span class="price">€ 35,00</span></div>
      <div class="row"><span class="svc">Nibh cursus</span><span class="dur">75 min</span><span class="price">€ 46,50</span></div>
      <div class="row"><span class="svc">Bibendum turpis</span><span class="dur">60 min</span><span class="price">€ 39,50</span></div>
      <div class="row"><span class="svc">sollicitudin</span><span class="dur">45 min</span><span class="price">€ 20,00</span></div>
      <div class="row"><span class="svc">Curabitur orci ipsum</span><span class="dur">35 min</span><span class="price">€ 35,00</span></div>
    </div>
  </div>

  <p class="intro">Lorem ipsum dolor sit amet, consectetur adipiscing elit. Duis ultricies ante in nibh cursus, nec bibendum turpis sollicitudin. Curabitur orci ipsum, cursus nec lorem quis, sodales malesuada dolor. Fusce facilisis erat in augue interdum gravida. Sed quis ipsum sapien. Donec posuere malesuada sagittis. In et ullamcorper elit. Curabitur ornare cursus pharetra. Mauris sed magna at magna tempus bibendum. Nulla ullamcorper auctor nibh, quis tristique mi ultricies vel.</p>
  <div class="signature">Fresh Start</div>
  <div class="subtitle">Kennenlern-Behandlung</div>
  <div class="brand brand--small" style="left:1010px;top:570px;width:140px">
    <div class="name">Lumara</div>
    <div class="tag">PFLEGE UND GELASSENHEIT</div>
  </div>
</section>

</body>
</html>
```